Radiant Crossroads - An Exciting Mission & Book Cover Project

Help me to inspire people to live their best life! This is a mission, not just a design project.
I need a Book Cover designed to keep me inspired on the process of writing my book.
Book Title: Radiant Crossroads
Tag Line: Three Simple Steps to get out of your own way, SuperCharge your Life and Step into Purpose!
Author: Marlon Teague

The three steps are: Ownership, Vision and Action (Not sure if this should be on the front or back of the book cover)

The book is a self-help, motivational book. Personal development.
The cover needs to be strong and capture peoples attention, especially with competing shelf space. I almost see a fire ball of flame or explosion that will grab peoples attention.
My company is The Summit Collective. I have added the company logo and a few pages of my presentation and topic outline to give an idea.
Maybe: The Summit Collective logo on back of the cover. website is marlonteague-example.com

THOUGHT: People should be able to take a photo of them holding the book cover showing what area of life they want Radiant Crossroads in. This is why the front cover must be so visual and powerful that they want to take a photo with it. Ie. Explosion, fire, strong and bold.

Target Market(s)

Anyone who feels stuck and needs to breakthrough and move forward in life.

Industry/Entity Type

Motivation

Font styles to use
Serif
Sans Serif

Colors
ec1f27
f37122
fbed22

Requirements
Must have
• The design must be STRONG, SIMPLE, STAND OUT ON BOOK SHELVES.
Must have an open file to swap the photo and copy out.

Back Cover Page
1) Summary
2) 2-3 testimonials. One sentence.
3) About the Author (maybe with photo)
4) Summit Collective logo
5) Website: radiantcrossroads-example.com and marlonteague-example.com
Nice to have
• If my photo works somewhere that would be great. I will change the photo later.
Added Where Does Your Compass Point? a nice cover example.
Should not have
• Right now I am writing the summary for the back of the cover. For now use Loreum Ipsum text and 2-3 recommendations. Again, I will get these only later.

```html
<!DOCTYPE html>
<html lang="en">
<head>
<meta charset="utf-8">
<title>Radiant Crossroads – Front Cover</title>
<link rel="stylesheet" href="https://fonts.googleapis.com/css2?family=Oswald:wght@500;700&display=swap">
<style>
  :root {
    --page-bg: #ffffff;
    --cover-black: #1f1d1e;
    --cover-sheen: #4a4647;
    --title-red: #e31e26;
    --author-yellow: #f5e01c;
    --burst-yellow: #fbe12a;
    --burst-orange: #f59a2c;
    --burst-red: #ec4a3a;
  }
  * { margin: 0; padding: 0; box-sizing: border-box; }
  html, body {
    width: 1200px;
    height: 1200px;
    overflow: hidden;
    background: var(--page-bg);
  }
  .canvas {
    position: relative;
    width: 1200px;
    height: 1200px;
  }
  .front-cover {
    position: absolute;
    left: 230px;
    top: 45px;
    width: 740px;
    height: 1110px;
    background:
      radial-gradient(ellipse 70% 45% at 0% 0%, var(--cover-sheen) 0%, rgba(74,70,71,0) 70%),
      var(--cover-black);
    overflow: hidden;
  }
  .cover-burst {
    position: absolute;
    left: 45px;
    top: 90px;
    width: 640px;
    height: 580px;
    border-radius: 50%;
    background: radial-gradient(circle at 52% 50%,
      var(--burst-red) 0%,
      var(--burst-orange) 22%,
      var(--burst-yellow) 48%,
      rgba(245,154,44,0.55) 66%,
      rgba(236,74,58,0) 78%);
  }
  .cover-title {
    position: absolute;
    left: 0;
    top: 715px;
    width: 740px;
    height: 130px;
  }
  .cover-title text {
    font-family: "Oswald", "Arial Narrow", sans-serif;
    font-weight: 500;
    fill: var(--title-red);
  }
  .cover-author {
    position: absolute;
    left: 0;
    top: 880px;
    width: 740px;
    text-align: center;
    padding-left: 30px;
    font-family: "Oswald", "Arial Narrow", sans-serif;
    font-weight: 700;
    font-size: 60px;
    line-height: 1;
    color: var(--author-yellow);
  }
</style>
</head>
<body>
  <main class="canvas">
    <section class="front-cover">
      <div class="cover-burst" role="img" aria-label="Illustration of a bright yellow, orange and red powder explosion bursting outward"></div>
      <svg class="cover-title" viewBox="0 0 740 130" aria-label="Radiant Crossroads">
        <text x="40" y="122" font-size="150" textLength="660" lengthAdjust="spacingAndGlyphs">RADIANT CROSSROADS</text>
      </svg>
      <p class="cover-author">Marlon Teague</p>
    </section>
  </main>
</body>
</html>
```